Brighter House Storage Scheme Email marketing campaign for Tamsel Energy

Design a visually engaging and professional marketing email to promote the upcoming National Cell Storage Grant to our existing solar clients, encouraging them to install a battery system now to maximise savings. email content example "Subject: ⚡ National Cell Storage Grant is Coming – Maximise Your Solar Savings

Body:
Hi [First Name],

Great news! With the federal election now decided, the National Household Cell Grant Initiative is officially on the way.

While the scheme hasn’t formally launched yet, it's guaranteed—and like the solar rebate before it, the subsidy reduces each year, so the earlier you install, the more you’ll save.

Crucially, the subsidy is only available once per household, so it makes sense to install a system that fully meets your home's battery needs right from the start.

Why add a battery to your existing solar system now?
✅ Store your excess solar energy instead of sending it back to the grid for low feed-in tariffs
✅ Use your stored solar power at night, when electricity prices are highest (typically 5–8pm)
✅ Slash your power bills and avoid rising time-of-use charges
✅ Protect your home from power outages
✅ Increase your self-sufficiency and long-term energy security

If you’ve already installed solar with us, now is the ideal time to complete your setup with a battery system designed to maximise your return—and take full advantage of this one-off federal subsidy.

Call us today or reply to this email to secure your spot and beat the rush.

Let your solar work smarter for your home,
The Tamsel Energy Team"

Target Market(s)

Content: We’ve provided the copy (see attached or below). The key points to emphasise in the design are: The urgency (subsidy winds down each year, limited to one per household). The benefits of installing a battery now, including energy savings, time-of-use charge avoidance, and self-sufficiency. Call to action: “Call us today or reply to this email to secure your spot and beat the rush.”

Industry/Entity Type

Renewable Energy

Colors
0054AA
0677BA
7BADD7
CADEEF
E8F1F8
EB3D1F
EC4F4E
F09395
F8D3D4
FCEDEE

Requirements
Must have
• Clean, modern, and trustworthy – aligned with Tamsel Energy branding. Bold headers and icons to make key points stand out. Include visual elements such as: A solar battery image Infographic or icon-style section showing key battery benefits (e.g. bill savings, backup power, self-consumption) Highlighted call-to-action button (“Secure My Battery Now” or “Beat the Rush”)
Nice to have
• I would like to have our company imagery (Tamsel Energy) alongside the battery brands we offer being Borvo, KWM, Velimar and QuintaPWR
Should not have
• Unsure

```html
<!DOCTYPE html>
<html lang="en">
<head>
<meta charset="utf-8">
<title>National Cell Storage Grant – Tamsel Energy</title>
<link rel="stylesheet" href="https://fonts.googleapis.com/css2?family=Figtree:wght@400;500;600;700;800&display=swap">
<style>
  :root {
    --page-bg: #f4f5f6;
    --card-bg: #ffffff;
    --brand-navy: #14315c;
    --brand-blue: #0677BA;
    --banner-blue: #2775b6;
    --deep-blue: #0054AA;
    --sky-light: #CADEEF;
    --sky-pale: #E8F1F8;
    --accent-orange: #ff7a00;
    --ink: #1c2430;
    --rule: #dfe8f1;
    --partner-grey: #7a7d82;
  }
  * { box-sizing: border-box; margin: 0; padding: 0; }
  html, body { width: 799px; height: 1200px; overflow: hidden; }
  body {
    background: var(--page-bg);
    font-family: "Figtree", Arial, sans-serif;
    color: var(--ink);
    position: relative;
  }
  .email-card {
    position: absolute;
    left: 43px; top: 30px;
    width: 713px; height: 1140px;
    background: var(--card-bg);
    box-shadow: 0 2px 10px rgba(0,0,0,0.08);
  }
  .brand {
    position: absolute; left: 59px; top: 33px; height: 43px;
    display: flex; align-items: center; gap: 10px;
  }
  .brand-dot { width: 30px; height: 30px; border-radius: 50%; background: var(--accent-orange); }
  .brand-name { font-size: 36px; font-weight: 800; color: var(--brand-navy); letter-spacing: 0.5px; }

  .hero-banner {
    position: absolute; left: 0; top: 106px; width: 713px; height: 190px;
    background: var(--banner-blue);
    display: flex; align-items: center; justify-content: center;
  }
  .hero-title {
    color: #fff; text-align: center; font-weight: 600;
    font-size: 38px; line-height: 48px; letter-spacing: 0.2px;
  }
  .hero-title svg { width: 28px; height: 38px; vertical-align: -5px; margin-right: 10px; }

  .greeting { position: absolute; left: 59px; top: 326px; font-size: 18px; font-weight: 600; }
  .urgency-tag {
    position: absolute; left: 59px; top: 374px; width: 245px; height: 35px;
    background: var(--accent-orange); border-radius: 6px;
    color: #fff; font-size: 16px; font-weight: 700;
    display: flex; align-items: center; justify-content: center; letter-spacing: -0.2px;
  }
  .intro {
    position: absolute; left: 59px; top: 420px; width: 350px;
    font-size: 16.5px; line-height: 25px;
  }
  .benefits-heading { position: absolute; left: 59px; top: 527px; }
  .benefits-heading .lead { font-size: 19px; font-weight: 600; display: block; line-height: 26px; }
  .benefits-heading .sub { font-size: 16px; font-weight: 500; text-transform: uppercase; display: block; line-height: 26px; }

  .benefit-list { position: absolute; left: 59px; top: 595px; list-style: none; }
  .benefit-list li {
    height: 46.5px; display: flex; align-items: center; gap: 16px;
    font-size: 18px; font-weight: 500;
  }
  .benefit-list svg { width: 40px; height: 40px; flex: none; }

  .section-rule { position: absolute; left: 59px; top: 841px; width: 339px; height: 1px; background: var(--rule); }
  .tagline { position: absolute; left: 59px; top: 867px; font-size: 21px; font-weight: 600; letter-spacing: 0.3px; }

  .battery-visual {
    position: absolute; left: 433px; top: 374px; width: 224px; height: 333px;
    border-radius: 8px;
    background: linear-gradient(160deg, var(--sky-pale) 0%, var(--sky-light) 60%, #b7d2ec 100%);
  }
  .grant-callout {
    position: absolute; left: 431px; top: 727px; width: 225px; height: 181px;
    background: var(--banner-blue); border-radius: 8px;
    box-shadow: 2px 4px 8px rgba(0,0,0,0.2);
    color: #fff; font-size: 17px; line-height: 22.6px; padding: 24px 10px 0 23px;
  }
  .cta-button {
    position: absolute; left: 59px; top: 927px; width: 597px; height: 61px;
    background: var(--accent-orange); border-radius: 6px;
    color: #fff; font-size: 22px; font-weight: 700; text-decoration: none;
    display: flex; align-items: center; justify-content: center; letter-spacing: -0.3px;
  }
  .footer-rule { position: absolute; left: 59px; top: 1016px; width: 597px; height: 1px; background: var(--rule); }
  .partner-brands {
    position: absolute; left: 59px; top: 1045px; width: 597px; height: 32px;
  }
  .partner {
    position: absolute; top: 0; line-height: 32px;
    font-size: 24px; font-weight: 600; color: var(--partner-grey); letter-spacing: 0.5px;
  }
  .partner-borvo { left: 5px; }
  .partner-kwm { left: 130px; }
  .partner-velimar { left: 240px; }
  .partner-quinta { left: 440px; }
</style>
</head>
<body>
  <main class="email-card">
    <div class="brand">
      <span class="brand-dot"></span>
      <span class="brand-name">TAMSEL</span>
    </div>

    <header class="hero-banner">
      <h1 class="hero-title">
        <svg viewBox="0 0 28 38" aria-hidden="true"><path d="M18 1 L3 22 H13 L9 37 L25 14 H15 Z" fill="#ff7a00"/></svg>NATIONAL CELL STORAGE<br>GRANT IS COMING –<br>MAXIMISE YOUR SOLAR SAVINGS
      </h1>
    </header>

    <p class="greeting">Hi (First Name),</p>
    <div class="urgency-tag">NEW SUBSIDY – ACT FAST</div>
    <p class="intro">Great news! With the federal election now decided, the National Household Cell Grant Initiative is officially on the way.</p>

    <h2 class="benefits-heading">
      <span class="lead">Why add a battery to your existing</span>
      <span class="sub">Solar system now?</span>
    </h2>

    <ul class="benefit-list">
      <li>
        <svg viewBox="0 0 40 40" fill="none" stroke="#0677BA" stroke-width="2.4" stroke-linejoin="round" stroke-linecap="round"><path d="M5 19 L20 5 L35 19"/><path d="M9 16 V34 H31 V16"/><path d="M14 22 L19 27 L27 18"/></svg>
        Store excess solar power
      </li>
      <li>
        <svg viewBox="0 0 40 40" fill="none" stroke="#0677BA" stroke-width="2.4" stroke-linecap="round"><path d="M17 7 A13 13 0 1 0 32 24 A10 10 0 0 1 17 7 Z"/><path d="M28 33 L33 28"/></svg>
        Use solar at night, cut charges
      </li>
      <li>
        <svg viewBox="0 0 40 40" fill="none" stroke="#0677BA" stroke-width="2.4" stroke-linejoin="round"><path d="M6 35 H35"/><rect x="9" y="24" width="5" height="11"/><rect x="18" y="17" width="5" height="18"/><rect x="27" y="9" width="5" height="26"/></svg>
        Lower your energy bills
      </li>
      <li>
        <svg viewBox="0 0 40 40" fill="none" stroke="#0677BA" stroke-width="2.4" stroke-linejoin="round"><path d="M20 4 L34 9 V20 C34 28 28 33 20 36 C12 33 6 28 6 20 V9 Z"/><path d="M22 11 L15 21 H21 L18 29 L26 18 H20 Z"/></svg>
        Backup during power outages
      </li>
      <li>
        <svg viewBox="0 0 40 40" fill="none" stroke="#0677BA" stroke-width="2.4" stroke-linecap="round" stroke-linejoin="round"><circle cx="20" cy="20" r="15"/><path d="M13 21 L18 26 L28 14"/></svg>
        Energy independence
      </li>
    </ul>

    <div class="section-rule"></div>
    <p class="tagline">LET YOUR SOLAR WORK SMARTER</p>

    <div class="battery-visual" role="img" aria-label="Photo of a white wall-mounted home energy storage battery unit"></div>

    <aside class="grant-callout">The subsidy reduces each year and is limited to one per household – installing a battery now ensures you don’t miss out!</aside>

    <a class="cta-button" href="#">BEAT THE RUSH – RESERVE MY BATTERY</a>

    <div class="footer-rule"></div>
    <div class="partner-brands">
      <span class="partner partner-borvo">Borvo</span>
      <span class="partner partner-kwm">KWM</span>
      <span class="partner partner-velimar">Velimar</span>
      <span class="partner partner-quinta">QuintaPWR</span>
    </div>
  </main>
</body>
</html>
```